BUSINESS CARD MIRELLE CAVANOSI

I need a new business card for my personal business.
I am a Naturopath and Nutritionist working doing private consults in the health and wellness arena.
I would like to see designs that are, clean minimalist but colourful.
I like:
White (clean,fresh, minimalist)
pops of one colour ONLY.Choose a colour to run with and keep it simple.
green
light blue
mustard
Bright yellow
Charcoal
The final design should communicate professionalism but also be in touch with nature.
Key Information to include:
MIRELLE CAVANOSI
ABN 48 217 603 915
RQTLBE 327081
Tel 0487 639 142
NATUROPATH | HERBALIST | NUTRITON CONSULTANT
BHSc (Naturopathic Studies) Grad Dip (Naturopathy)
BACK OF CARD : YOUR NEXT APPOINTMENT ..................................
I already have a logo (picture attached)But I would be more than happy to NOT have this included. I am very Open to cards WITHOUT current logo/ ones that weave the colour of my logo but do not use the logo.
I have included pictures attached to give examples of the styles/colors I enjoy.
Updates
I have added a picture of a mortar and pestle - one just like this would be lovely to include in your entry.
TIA

```html
<!DOCTYPE html>
<html lang="en">
<head>
<meta charset="utf-8">
<title>Mirelle Cavanosi Naturopathy – Business Card</title>
<link href="https://fonts.googleapis.com/css2?family=Raleway:wght@300;400;600;700&display=swap" rel="stylesheet">
<style>
  :root {
    --bg: #e9eae8;
    --card-white: #f4f4f3;
    --card-grey: #d9dad8;
    --green-dark: #1d7a2e;
    --green: #2f9a3a;
    --green-light: #7cc242;
    --lime: #c7dd3a;
    --charcoal: #3b3d3c;
    --text-grey: #6b6d6c;
    --white: #ffffff;
  }
  * { box-sizing: border-box; margin: 0; padding: 0; }
  html, body {
    width: 1200px; height: 1001px; overflow: hidden;
    background: var(--bg);
    font-family: "Raleway", "Helvetica Neue", Arial, sans-serif;
  }
  .card {
    position: absolute; left: 220px;
    width: 760px; height: 463px;
    border-radius: 22px; overflow: hidden;
    background: var(--card-white);
    box-shadow: 0 6px 18px rgba(0,0,0,0.12);
  }
  .card--details { top: 24px; }
  .card--front { top: 514px; }
  .card__art { position: absolute; inset: 0; width: 100%; height: 100%; }

  .details {
    position: absolute; left: 300px; top: 128px;
    color: var(--text-grey); font-size: 14px; line-height: 1.75;
  }
  .details__name {
    color: var(--green); font-weight: 700; font-size: 22px;
    letter-spacing: 0.5px; margin-bottom: 8px;
  }

  .brand {
    position: absolute; left: 258px; top: 168px;
  }
  .brand__name {
    color: var(--charcoal); font-weight: 400; font-size: 36px;
    letter-spacing: 6px; line-height: 1;
  }
  .brand__field {
    color: var(--green); font-weight: 400; font-size: 22px;
    letter-spacing: 15px; margin-top: 14px;
  }
  .tagline {
    position: absolute; right: 26px; top: 372px;
    color: var(--white); font-size: 14px; letter-spacing: 0.3px;
    white-space: nowrap;
  }
</style>
</head>
<body>

<section class="card card--details">
  <svg class="card__art" viewBox="0 0 760 463">
    <defs>
      <linearGradient id="detailsGreen" x1="0" y1="0" x2="1" y2="1">
        <stop offset="0" stop-color="#3fae3c"/>
        <stop offset="0.6" stop-color="#2b9634"/>
        <stop offset="1" stop-color="#1d7a2e"/>
      </linearGradient>
      <radialGradient id="detailsLeaves" cx="0.7" cy="0.35" r="0.7">
        <stop offset="0" stop-color="#f7f7f6"/>
        <stop offset="1" stop-color="#d8d9d7"/>
      </radialGradient>
    </defs>
    <rect width="760" height="463" fill="url(#detailsLeaves)" role="img" aria-label="Soft grey leaf pattern background"/>
    <path d="M0 0 H360 C280 50 200 200 215 463 H0 Z" fill="#c9e08a"/>
    <path d="M0 0 H340 C262 50 184 200 196 463 H0 Z" fill="#ffffff" opacity="0.9"/>
    <path d="M0 0 H325 C248 50 170 200 180 463 H0 Z" fill="url(#detailsGreen)"/>
    <circle cx="150" cy="232" r="52" fill="var(--white)"/>
    <circle cx="150" cy="232" r="40" fill="var(--green)"/>
  </svg>
  <div class="details">
    <p class="details__name">MIRELLE CAVANOSI NATUROPATH</p>
    <p>ABN 48 217 603 915</p>
    <p>RQTLBE 327081</p>
    <p>Tel 0487 639 142</p>
    <p>Naturopath | Herbalist | Nutrition consultant</p>
    <p>BHSc (Naturopathic Studies) Grad Dip (Naturopathy)</p>
  </div>
</section>

<section class="card card--front">
  <svg class="card__art" viewBox="0 0 760 463">
    <defs>
      <radialGradient id="frontLeaves" cx="0.45" cy="0.35" r="0.75">
        <stop offset="0" stop-color="#f5f5f4"/>
        <stop offset="1" stop-color="#cfd0ce"/>
      </radialGradient>
      <linearGradient id="frontBand" x1="0" y1="0" x2="1" y2="0">
        <stop offset="0" stop-color="#4fb043"/>
        <stop offset="1" stop-color="#1d7a2e"/>
      </linearGradient>
    </defs>
    <rect width="760" height="463" fill="url(#frontLeaves)" role="img" aria-label="Soft grey leaf pattern background"/>
    <path d="M0 463 V372 C260 330 520 300 760 250 V463 Z" fill="var(--lime)"/>
    <path d="M0 463 V388 C260 346 520 318 760 270 V463 Z" fill="#ffffff" opacity="0.85"/>
    <path d="M0 463 V400 C260 360 520 332 760 284 V463 Z" fill="url(#frontBand)"/>
    <circle cx="172" cy="206" r="58" fill="var(--white)"/>
    <circle cx="172" cy="206" r="45" fill="var(--green)"/>
  </svg>
  <div class="brand">
    <p class="brand__name">MIRELLE CAVANOSI</p>
    <p class="brand__field">NATUROPATHY</p>
  </div>
  <p class="tagline">Naturopath | Herbalist | Nutrition consultant</p>
</section>

</body>
</html>
```